NEW YORK Plumbing/utility company 10 year anniversary business card

Looking For simple back and front business card would like to include a few things in description
We offer 24/7 emergency service
residential
commercial
industrial
municipal
services offered
Plumbing
hydro excavation
hydro jetting
Well pumps
Sewer pumps
water mains
sewer mains

```html
<!DOCTYPE html>
<html lang="en">
<head>
<meta charset="utf-8">
<title>Ridgeline Water &amp; Sewer — 10th Anniversary Business Card</title>
<link rel="stylesheet" href="https://fonts.googleapis.com/css2?family=Montserrat:wght@500;600;700;800&family=Oswald:wght@600&family=Lobster&display=swap">
<style>
  :root {
    --stage: #3b3b3d;
    --brand-blue: #0f62a8;
    --brand-blue-deep: #0a4f8c;
    --sky-blue: #2ea6e8;
    --paper: #ffffff;
    --ink-light: #ffffff;
  }
  * { box-sizing: border-box; margin: 0; padding: 0; }
  html, body {
    width: 1200px; height: 900px; overflow: hidden;
    background: var(--stage);
    font-family: "Montserrat", sans-serif;
  }
  .canvas {
    width: 1200px; height: 900px;
    display: flex; flex-direction: column;
    align-items: center; justify-content: center; gap: 56px;
  }
  .card {
    position: relative;
    width: 640px; height: 366px;
    border-radius: 20px;
    overflow: hidden;
  }

  /* Front */
  .card--front { background: var(--paper); }
  .brand-name {
    position: absolute;
    display: flex; align-items: center; gap: 14px;
    font-weight: 800; letter-spacing: 2px; line-height: 1.15;
    text-transform: uppercase;
    white-space: nowrap;
  }
  .brand-name__dot {
    width: 18px; height: 18px; border-radius: 50%; flex: none;
  }
  .card--front .brand-name { left: 60px; top: 108px; color: var(--brand-blue); font-size: 28px; }
  .card--front .brand-name__dot { background: var(--brand-blue); }

  .anniversary-ribbon { position: absolute; right: 70px; top: 0; width: 96px; height: 130px; }
  .anniversary-ribbon__number {
    position: absolute; right: 70px; top: 26px; width: 96px;
    text-align: center; color: var(--ink-light);
    font-family: "Oswald", sans-serif; font-weight: 600; font-size: 46px; line-height: 1;
  }
  .anniversary-ribbon__number sup { font-size: 16px; vertical-align: top; margin-left: 2px; }
  .anniversary-script {
    position: absolute; right: 36px; top: 140px;
    font-family: "Lobster", cursive; font-size: 34px; color: var(--brand-blue);
  }

  .emergency-line {
    position: absolute; left: 40px; bottom: 104px;
    font-weight: 700; font-size: 20px; color: var(--brand-blue-deep);
    letter-spacing: 0.5px; text-transform: uppercase;
  }
  .sector-rule { position: absolute; left: 0; right: 0; bottom: 82px; height: 5px; background: var(--sky-blue); }
  .sector-band {
    position: absolute; left: 0; right: 0; bottom: 0; height: 82px;
    background: var(--brand-blue);
    display: flex; align-items: center; gap: 26px; padding-left: 40px;
  }
  .sector-band__item, .service-list__item {
    display: flex; align-items: center; gap: 7px;
    color: var(--ink-light); font-weight: 500; text-transform: uppercase;
  }
  .sector-band__item { font-size: 17px; }
  .drop { width: 9px; height: 13px; flex: none; }

  /* Back */
  .card--back { background: linear-gradient(135deg, #1470b8 0%, var(--brand-blue) 55%, var(--brand-blue-deep) 100%); }
  .card--back .brand-name { left: 40px; top: 122px; color: var(--ink-light); font-size: 26px; }
  .card--back .brand-name__dot { background: var(--ink-light); }
  .services { position: absolute; left: 385px; top: 70px; }
  .services__title {
    color: var(--ink-light); font-weight: 600; font-size: 20px;
    text-transform: uppercase; letter-spacing: 0.5px; margin-bottom: 10px;
  }
  .service-list { list-style: none; display: flex; flex-direction: column; gap: 5px; }
  .service-list__item { font-size: 16px; }
</style>
</head>
<body>
<main class="canvas">

  <section class="card card--front" aria-label="Business card front">
    <div class="brand-name"><span class="brand-name__dot"></span><span>Ridgeline<br>Water &amp; Sewer</span></div>

    <svg class="anniversary-ribbon" viewBox="0 0 96 130" aria-hidden="true">
      <polygon points="0,0 96,0 96,122 48,96 0,122" fill="#2ea6e8"/>
      <polygon points="0,0 96,0 96,114 48,88 0,114" fill="#0f62a8"/>
    </svg>
    <div class="anniversary-ribbon__number">10<sup>TH</sup></div>
    <div class="anniversary-script">Anniversary</div>

    <p class="emergency-line">We offer 24/7 emergency service</p>
    <div class="sector-rule"></div>
    <div class="sector-band">
      <span class="sector-band__item"><svg class="drop" viewBox="0 0 10 14"><path d="M5 0C5 0 0 6 0 9a5 5 0 0 0 10 0C10 6 5 0 5 0Z" fill="#fff"/></svg>Residential</span>
      <span class="sector-band__item"><svg class="drop" viewBox="0 0 10 14"><path d="M5 0C5 0 0 6 0 9a5 5 0 0 0 10 0C10 6 5 0 5 0Z" fill="#fff"/></svg>Commercial</span>
      <span class="sector-band__item"><svg class="drop" viewBox="0 0 10 14"><path d="M5 0C5 0 0 6 0 9a5 5 0 0 0 10 0C10 6 5 0 5 0Z" fill="#fff"/></svg>Industrial</span>
      <span class="sector-band__item"><svg class="drop" viewBox="0 0 10 14"><path d="M5 0C5 0 0 6 0 9a5 5 0 0 0 10 0C10 6 5 0 5 0Z" fill="#fff"/></svg>Municipal</span>
    </div>
  </section>

  <section class="card card--back" aria-label="Business card back">
    <div class="brand-name"><span class="brand-name__dot"></span><span>Ridgeline<br>Water &amp; Sewer</span></div>
    <div class="services">
      <h2 class="services__title">Services offered</h2>
      <ul class="service-list">
        <li class="service-list__item"><svg class="drop" viewBox="0 0 10 14"><path d="M5 0C5 0 0 6 0 9a5 5 0 0 0 10 0C10 6 5 0 5 0Z" fill="#fff"/></svg>Plumbing</li>
        <li class="service-list__item"><svg class="drop" viewBox="0 0 10 14"><path d="M5 0C5 0 0 6 0 9a5 5 0 0 0 10 0C10 6 5 0 5 0Z" fill="#fff"/></svg>Hydro excavation</li>
        <li class="service-list__item"><svg class="drop" viewBox="0 0 10 14"><path d="M5 0C5 0 0 6 0 9a5 5 0 0 0 10 0C10 6 5 0 5 0Z" fill="#fff"/></svg>Hydro jetting</li>
        <li class="service-list__item"><svg class="drop" viewBox="0 0 10 14"><path d="M5 0C5 0 0 6 0 9a5 5 0 0 0 10 0C10 6 5 0 5 0Z" fill="#fff"/></svg>Well pumps</li>
        <li class="service-list__item"><svg class="drop" viewBox="0 0 10 14"><path d="M5 0C5 0 0 6 0 9a5 5 0 0 0 10 0C10 6 5 0 5 0Z" fill="#fff"/></svg>Sewer pumps</li>
        <li class="service-list__item"><svg class="drop" viewBox="0 0 10 14"><path d="M5 0C5 0 0 6 0 9a5 5 0 0 0 10 0C10 6 5 0 5 0Z" fill="#fff"/></svg>Water mains</li>
        <li class="service-list__item"><svg class="drop" viewBox="0 0 10 14"><path d="M5 0C5 0 0 6 0 9a5 5 0 0 0 10 0C10 6 5 0 5 0Z" fill="#fff"/></svg>Sewer mains</li>
      </ul>
    </div>
  </section>

</main>
</body>
</html>
```